Verpackungen für Kosmetikhersteller
Zielgruppe
DE:
Wir sind ein junges Unternehmen, welches Kosmetik auf Kokosnussölbasis herstellt. Als erstes Produkt möchten wir ein Mundziehöl in verschiedenen Geschmacksrichtungen auf den Markt bringen. Zielgruppe sind gesundheitsbewusste Konsumenten im mittleren bis höherem Einkommensbereich. Für das Mundziehöl suchen wir nun ein Verpackungsdesign. Das Öl wird in Stickpacks zu 10 ml im Grundformat 30x110mm abgepackt (Skizze mit genauen Abstandsangaben im Anhang). Beispiele eines Stickpacks sind im Anhang als Stickpack example und Stickpack example2 hochgeladen. Neben unserem Loge sollte eine Angabe über die Geschmacksrichtung ebenfalls Platz auf der Verpackung finden.
EN:
We are a young start up, producing cosmetics based on coconut oil. As a first product we want to introduce a mouth pulling oil into the market. The oil will be sold in different flavors. The targeted consumer is a health conscious young adult in the middle to upper income range. The product will be filled in stickpacks (30x110mm) a 10 ml per pack. An example of an stick pack you can see as stickpack_example and stickpack_example2. The exact format, with dimensions you can see in the attachment skizze_30x110. The stickpack should show a simple and modern design however reflecting a high quality product for the health conscious consumer. The content should be our logo, the name of the product 'mirovalle' a feature which shows the flavor and a symbol or other feature to show that the product is coconut based. The design should not be overloaded. Simplicity but high class design is desirable.
Flavors are:
Pfefferminze (pepermint)
Limette (lime)
Zitrone (lemon)
Orange (orange)
Melisse (melissa)
Melisse / Orange (melissa/orange)
Blutorange (blood orange)
Fenchel (fennel)
Vanille (vanilla)
Zimt (cinnamon)
Aufgabenstellung
Das Design des Stickpacks sollte den jungen, gesundheitsbewussten Konsumenten ansprechen. Es sollte schlicht und modern gestaltet sein wobei erkennbar werden muss, dass es sich um ein höherpreisiges Qualitätsprodukt handelt. Es sollte weiterhin bemerkbar sein, dass der Grundstoff Kokosöl ist. Über ein einzelnes Feature sollte weiterhin erkennbar sein, um welche Geschmacksrichtung es sich handelt. Es sollen folgende Geschmacksrichtungen angeboten werden:
Pfefferminze
Limette
Zitrone
Orange
Melisse
Melisse / Orange
Blutorange
Fenchel
Vanille
Zimt
Der Name des Produktes, 'Mirovalle' sollte auch auf dem Stickpack ersichtlich sein, muss aber nicht zwingend im Mittelpunkt der Verpackung stehen.
Das Design sollte harmonisch wirken und nicht allzu große farbliche Kontraste aufweisen. Bilder von Kokosnüssen oder Palmen sowie weißer Zähne können gern eingearbeitet werden.

```html
<!DOCTYPE html>
<html lang="de">
<head>
<meta charset="utf-8">
<title>Mirovalle Stickpacks</title>
<link href="https://fonts.googleapis.com/css2?family=Oswald:wght@500;600&family=Open+Sans:wght@400;700&display=swap" rel="stylesheet">
<style>
  :root {
    --brand-green: #1f8a3a;
    --bg: #ffffff;
    --foil-light: #fbfbfb;
    --foil-mid: #e9e9ea;
    --foil-dark: #d3d3d5;
    --cut-line: #e5178f;
    --text-dark: #333333;
    --coconut: #b08a66;
    --vanille: #dcdf93;
    --orange: #ef8a1e;
    --limette: #8cc63f;
    --zitrone: #d9d21b;
    --zimt: #e6955a;
    --melisse: #6db33f;
    --blutorange: #c1272d;
    --pfefferminze: #2e9e48;
  }
  html, body { margin: 0; padding: 0; overflow: hidden; }
  body { width: 1200px; height: 952px; background: var(--bg); position: relative; font-family: "Oswald", sans-serif; }

  .stickpack { position: absolute; width: 108px; height: 396px; }
  .stickpack__band { position: absolute; left: 0; right: 0; height: 27px; background: var(--c); }
  .stickpack__band--top { top: 0; }
  .stickpack__band--bottom { bottom: 0; height: 24px; }
  .stickpack__body {
    position: absolute; top: 27px; bottom: 24px; left: 6px; right: 6px;
    background: linear-gradient(90deg, var(--foil-dark) 0%, var(--foil-light) 18%, var(--foil-light) 55%, var(--foil-mid) 85%, var(--foil-dark) 100%);
  }
  .brand { position: absolute; left: 0; right: 0; text-align: center; font-family: "Oswald", sans-serif; font-weight: 600; color: var(--brand-green); }
  .stickpack .brand { top: 64px; font-size: 19px; }
  .product-name { position: absolute; left: 0; right: 0; text-align: center; font-weight: 600; color: var(--brand-green); letter-spacing: .5px; }
  .stickpack .product-name { top: 162px; font-size: 12px; }
  .flavor { position: absolute; left: 0; right: 0; text-align: center; font-weight: 600; color: var(--c); letter-spacing: 1px; line-height: 1; }
  .stickpack .flavor { top: 180px; font-size: 22px; }
  .stickpack .flavor--small { font-size: 14px; top: 185px; }
  .stickpack .flavor--tiny { font-size: 11px; top: 187px; letter-spacing: 0; }
  .flavor__sep { color: var(--text-dark); }
  .flavor__first { color: var(--melisse); }
  .visual {
    position: absolute; border-radius: 10px;
    background: linear-gradient(135deg, var(--c) 0%, var(--coconut) 100%);
    opacity: .55;
  }
  .stickpack .visual { top: 226px; left: 16px; width: 76px; height: 54px; }

  .label { position: absolute; width: 267px; height: 402px; background: #fff; border: 1px solid var(--cut-line); box-sizing: border-box; }
  .label__band { position: absolute; left: 0; right: 0; height: 22px; background: var(--c); }
  .label__band--top { top: 0; border-bottom: 1px solid var(--cut-line); }
  .label__band--bottom { bottom: 0; border-top: 1px solid var(--cut-line); }
  .label__fold { position: absolute; top: 22px; bottom: 22px; width: 1px; background: var(--cut-line); }
  .label__face { position: absolute; left: 91px; width: 91px; top: 22px; bottom: 22px; }
  .label .brand { top: 38px; font-size: 20px; }
  .label .product-name { top: 140px; font-size: 12px; }
  .label .flavor { top: 157px; font-size: 23px; }
  .label .visual { top: 206px; left: 6px; width: 78px; height: 56px; }
  .label__info {
    position: absolute; left: 186px; top: 36px; height: 336px;
    writing-mode: vertical-rl; transform: rotate(180deg);
    font-family: "Open Sans", sans-serif; font-size: 7.6px; line-height: 10px; color: var(--text-dark);
  }
  .label__info strong { font-weight: 700; }
  .label__volume {
    position: absolute; left: 224px; top: 36px; writing-mode: vertical-rl; transform: rotate(180deg);
    font-family: "Open Sans", sans-serif; font-weight: 700; font-size: 8px; color: var(--text-dark);
  }
  .label__recycle { position: absolute; left: 218px; top: 78px; width: 14px; height: 14px; }
</style>
</head>
<body>

  <div class="stickpack" style="left:41px; top:40px; --c:var(--vanille)">
    <div class="stickpack__band stickpack__band--top"></div>
    <div class="stickpack__body"></div>
    <div class="brand">Kokovera</div>
    <div class="product-name">MIROVALLE</div>
    <div class="flavor">VANILLE</div>
    <div class="visual" role="img" aria-label="Foto: Kokosnuss mit Vanilleschoten und Blüte"></div>
    <div class="stickpack__band stickpack__band--bottom"></div>
  </div>

  <div class="stickpack" style="left:188px; top:40px; --c:var(--orange)">
    <div class="stickpack__band stickpack__band--top"></div>
    <div class="stickpack__body"></div>
    <div class="brand">Kokovera</div>
    <div class="product-name">MIROVALLE</div>
    <div class="flavor">ORANGE</div>
    <div class="visual" role="img" aria-label="Foto: Kokosnuss mit Orangen"></div>
    <div class="stickpack__band stickpack__band--bottom"></div>
  </div>

  <div class="stickpack" style="left:336px; top:40px; --c:var(--limette)">
    <div class="stickpack__band stickpack__band--top"></div>
    <div class="stickpack__body"></div>
    <div class="brand">Kokovera</div>
    <div class="product-name">MIROVALLE</div>
    <div class="flavor">LIMETTE</div>
    <div class="visual" role="img" aria-label="Foto: Kokosnuss mit Limetten"></div>
    <div class="stickpack__band stickpack__band--bottom"></div>
  </div>

  <div class="stickpack" style="left:497px; top:40px; --c:var(--zitrone)">
    <div class="stickpack__band stickpack__band--top"></div>
    <div class="stickpack__body"></div>
    <div class="brand">Kokovera</div>
    <div class="product-name">MIROVALLE</div>
    <div class="flavor">ZITRONE</div>
    <div class="visual" role="img" aria-label="Foto: Kokosnuss mit Zitronen"></div>
    <div class="stickpack__band stickpack__band--bottom"></div>
  </div>

  <div class="stickpack" style="left:650px; top:40px; --c:var(--zimt)">
    <div class="stickpack__band stickpack__band--top"></div>
    <div class="stickpack__body"></div>
    <div class="brand">Kokovera</div>
    <div class="product-name">MIROVALLE</div>
    <div class="flavor">ZIMT</div>
    <div class="visual" role="img" aria-label="Foto: Kokosnuss mit Zimtstangen"></div>
    <div class="stickpack__band stickpack__band--bottom"></div>
  </div>

  <div class="stickpack" style="left:115px; top:476px; --c:var(--melisse)">
    <div class="stickpack__band stickpack__band--top"></div>
    <div class="stickpack__body"></div>
    <div class="brand">Kokovera</div>
    <div class="product-name">MIROVALLE</div>
    <div class="flavor">MELISSE</div>
    <div class="visual" role="img" aria-label="Foto: Kokosnuss mit Melissenblättern"></div>
    <div class="stickpack__band stickpack__band--bottom"></div>
  </div>

  <div class="stickpack" style="left:266px; top:476px; --c:var(--blutorange)">
    <div class="stickpack__band stickpack__band--top"></div>
    <div class="stickpack__body"></div>
    <div class="brand">Kokovera</div>
    <div class="product-name">MIROVALLE</div>
    <div class="flavor flavor--small">BLUTORANGE</div>
    <div class="visual" role="img" aria-label="Foto: Kokosnuss mit Blutorangen"></div>
    <div class="stickpack__band stickpack__band--bottom"></div>
  </div>

  <div class="stickpack" style="left:425px; top:476px; --c:var(--pfefferminze)">
    <div class="stickpack__band stickpack__band--top"></div>
    <div class="stickpack__body"></div>
    <div class="brand">Kokovera</div>
    <div class="product-name">MIROVALLE</div>
    <div class="flavor flavor--small">PFEFFERMINZE</div>
    <div class="visual" role="img" aria-label="Foto: Kokosnuss mit Pfefferminzblättern"></div>
    <div class="stickpack__band stickpack__band--bottom"></div>
  </div>

  <div class="stickpack" style="left:574px; top:476px; --c:var(--orange)">
    <div class="stickpack__band stickpack__band--top"></div>
    <div class="stickpack__body"></div>
    <div class="brand">Kokovera</div>
    <div class="product-name">MIROVALLE</div>
    <div class="flavor flavor--tiny"><span class="flavor__first">MELISSE</span><span class="flavor__sep">/</span>ORANGE</div>
    <div class="visual" role="img" aria-label="Foto: Kokosnuss mit Orangen und Melisse"></div>
    <div class="stickpack__band stickpack__band--bottom"></div>
  </div>

  <div class="label" style="left:870px; top:30px; --c:var(--vanille)">
    <div class="label__band label__band--top"></div>
    <div class="label__fold" style="left:54px"></div>
    <div class="label__fold" style="left:91px"></div>
    <div class="label__fold" style="left:182px"></div>
    <div class="label__fold" style="left:242px"></div>
    <div class="label__face">
      <div class="brand">Kokovera</div>
      <div class="product-name">MIROVALLE</div>
      <div class="flavor">VANILLE</div>
      <div class="visual" role="img" aria-label="Foto: Kokosnuss mit Vanilleschoten und Blüte"></div>
    </div>
    <div class="label__info">Mundziehöl auf Kokosölbasis.<br><strong>Ingredients (INCI)</strong>: cocos nucifera oil, mentha spicata herb oil, mentha arvensis leaf oil<br>Mindestens haltbar bis: 10/2019<br>www.kokovera.de</div>
    <div class="label__volume">10 ml</div>
    <svg class="label__recycle" viewBox="0 0 20 20" aria-hidden="true"><circle cx="10" cy="10" r="7" fill="none" stroke="var(--brand-green)" stroke-width="3" stroke-dasharray="9 5"/></svg>
    <div class="label__band label__band--bottom"></div>
  </div>

  <div class="label" style="left:867px; top:467px; --c:var(--orange)">
    <div class="label__band label__band--top"></div>
    <div class="label__fold" style="left:54px"></div>
    <div class="label__fold" style="left:91px"></div>
    <div class="label__fold" style="left:182px"></div>
    <div class="label__fold" style="left:242px"></div>
    <div class="label__face">
      <div class="brand">Kokovera</div>
      <div class="product-name">MIROVALLE</div>
      <div class="flavor">ORANGE</div>
      <div class="visual" role="img" aria-label="Foto: Kokosnuss mit Orangen"></div>
    </div>
    <div class="label__info">Mundziehöl auf Kokosölbasis.<br><strong>Ingredients (INCI)</strong>: cocos nucifera oil, mentha spicata herb oil, mentha arvensis leaf oil<br>Mindestens haltbar bis: 10/2019<br>www.kokovera.de</div>
    <div class="label__volume">10 ml</div>
    <svg class="label__recycle" viewBox="0 0 20 20" aria-hidden="true"><circle cx="10" cy="10" r="7" fill="none" stroke="var(--brand-green)" stroke-width="3" stroke-dasharray="9 5"/></svg>
    <div class="label__band label__band--bottom"></div>
  </div>

</body>
</html>
```